Firm Stationery Design

I need a design for stationery, including: Stationery First Page, Stationery Second Sheet, Envelope, Mailing Label for Flat Envelopes, and Business Cards

```html
<!DOCTYPE html>
<html lang="en">
<head>
<meta charset="utf-8">
<title>Harlow Law LLC – Stationery</title>
<link href="https://fonts.googleapis.com/css2?family=Poppins:wght@400;500;600;700&display=swap" rel="stylesheet">
<style>
  :root{
    --canvas:#d9d9d9;
    --paper:#ffffff;
    --ink:#111a19;
    --ink-soft:#1a1a1a;
    --orange:#ffa000;
    --faint:#f1f1f1;
    --window:#666666;
    --text:#1f1f1f;
  }
  *{box-sizing:border-box;margin:0;padding:0}
  html,body{width:1014px;height:1200px;overflow:hidden;background:var(--canvas)}
  body{position:relative;font-family:"Poppins",sans-serif;color:var(--text)}
  .sheet{position:absolute;background:var(--paper);box-shadow:0 3px 10px rgba(0,0,0,.12);overflow:hidden}
  .sheet > svg.bands{position:absolute;inset:0;width:100%;height:100%}
  .letter-first{left:62px;top:68px;width:404px;height:522px}
  .letter-second{left:508px;top:68px;width:404px;height:522px}
  .envelope-front{left:62px;top:652px;width:404px;height:202px}
  .envelope-back{left:508px;top:652px;width:404px;height:202px}
  .card-front{left:232px;top:917px;width:233px;height:134px}
  .card-back{left:512px;top:917px;width:233px;height:134px}

  .brand{position:absolute;display:flex;align-items:center;gap:5px;
    font-weight:700;color:var(--ink);white-space:nowrap;letter-spacing:.02em}
  .brand .brand-square{display:inline-block;background:var(--orange);flex:none}
  .letter-first .brand,.letter-second .brand{left:39px;top:76px;font-size:13px}
  .letter-first .brand-square,.letter-second .brand-square{width:10px;height:10px}

  .letter-body{position:absolute;left:37px;top:134px;width:325px;font-size:6.6px;line-height:1.22;text-align:justify}
  .letter-body p{margin-bottom:7px}
  .letter-body p.greeting{margin-bottom:2px}
  .signature{position:absolute;left:251px;top:402px;width:106px;border-top:1px solid #dcdcdc;text-align:right;padding-top:6px}
  .signature .sig-name{font-size:10.5px;color:var(--ink);line-height:1.1}
  .signature .sig-name b{color:var(--orange);font-weight:600}
  .signature .sig-role{font-size:5.5px;text-align:center;padding-left:40px;margin-top:1px}

  .contact-row{position:absolute;left:37px;top:454px;display:flex;gap:7px;align-items:center;font-size:5.4px;font-weight:500;white-space:nowrap}
  .contact-row .item{display:flex;align-items:center;gap:3px}
  .contact-row .item.phone{font-size:6.6px}
  .ico{width:10px;height:10px;flex:none}

  .watermark{position:absolute;left:0;width:100%;text-align:center;font-weight:700;color:var(--faint);white-space:nowrap}
  .letter-second .watermark{top:318px;font-size:31px;letter-spacing:.03em}
  .site-foot{position:absolute;left:35px;top:490px;font-size:10px;color:#fff;font-weight:400}

  .envelope-front .brand{left:27px;top:58px;font-size:10.5px}
  .envelope-front .brand-square{width:8px;height:8px}
  .address-window{position:absolute;left:245px;top:50px;width:125px;height:45px;background:var(--window);border-radius:4px;border:1px solid #555}
  .env-contacts{position:absolute;font-size:6px;font-weight:500;display:flex;flex-direction:column;gap:5px;white-space:nowrap}
  .env-contacts .item{display:flex;align-items:center;gap:5px}
  .env-contacts.col-a{left:27px;top:124px}
  .env-contacts.col-b{left:146px;top:124px}
  .env-contacts .phone{font-size:7.2px}

  .envelope-back .brand{left:0;width:100%;justify-content:center;top:30px;font-size:10px;color:#fff}
  .envelope-back .brand-square{width:8px;height:8px}

  .card-front .pattern{position:absolute;left:0;top:0;width:110px;height:134px;
    background:radial-gradient(ellipse at 50% 40%,#2a2a2a 0%,#111 70%,#0b0b0b 100%)}
  .card-front .brand{left:0;width:110px;justify-content:center;top:60px;font-size:9px;color:#fff;flex-direction:column;gap:4px}
  .card-front .brand-square{width:14px;height:14px}
  .card-info{position:absolute;left:126px;top:26px}
  .card-info .name{font-size:10px;color:var(--ink);line-height:1.1}
  .card-info .name b{font-weight:600}
  .card-info .role{font-size:6.4px}
  .card-info ul{list-style:none;margin-top:10px;font-size:5.3px;display:flex;flex-direction:column;gap:3.5px}
  .card-info li{display:flex;align-items:center;gap:4px}
  .card-info .ico{width:7px;height:7px}

  .card-back .pattern{position:absolute;inset:0;
    background:radial-gradient(ellipse at 50% 50%,#262626 0%,#121212 60%,#070707 100%)}
  .card-back .brand{left:0;width:100%;justify-content:center;top:42px;font-size:11px;color:#fff;flex-direction:column;gap:6px}
  .card-back .brand-square{width:16px;height:16px}
  .card-back .site{position:absolute;left:0;width:100%;top:99px;text-align:center;color:#fff;font-size:9px;letter-spacing:.08em}
</style>
</head>
<body>

<svg width="0" height="0" style="position:absolute" aria-hidden="true">
  <defs>
    <symbol id="ico-phone" viewBox="0 0 20 20">
      <circle cx="10" cy="10" r="10" fill="#ffa000"/>
      <path d="M7 5.5l2 2-1.2 1.5c.8 1.5 1.7 2.4 3.2 3.2L12.5 11l2 2-1.3 1.8c-3.8-.4-7.6-4.2-8-8z" fill="#fff"/>
    </symbol>
    <symbol id="ico-pin" viewBox="0 0 20 20">
      <circle cx="10" cy="10" r="10" fill="#ffa000"/>
      <path d="M10 4.5a3.6 3.6 0 0 0-3.6 3.6c0 2.8 3.6 7 3.6 7s3.6-4.2 3.6-7A3.6 3.6 0 0 0 10 4.5z" fill="#fff"/>
      <circle cx="10" cy="8.1" r="1.3" fill="#ffa000"/>
    </symbol>
    <symbol id="ico-mail" viewBox="0 0 20 20">
      <circle cx="10" cy="10" r="10" fill="#ffa000"/>
      <rect x="5" y="6.5" width="10" height="7" fill="#fff"/>
      <path d="M5 6.5l5 4 5-4" fill="none" stroke="#ffa000" stroke-width="1"/>
    </symbol>
    <symbol id="ico-web" viewBox="0 0 20 20">
      <circle cx="10" cy="10" r="10" fill="#ffa000"/>
      <circle cx="10" cy="10" r="5" fill="none" stroke="#fff" stroke-width="1.1"/>
      <ellipse cx="10" cy="10" rx="2.2" ry="5" fill="none" stroke="#fff" stroke-width="1"/>
      <path d="M5 10h10" stroke="#fff" stroke-width="1"/>
    </symbol>
  </defs>
</svg>

<!-- First page -->
<section class="sheet letter-first">
  <svg class="bands" viewBox="0 0 702 908" preserveAspectRatio="none" aria-hidden="true">
    <rect x="0" y="43" width="62" height="64" fill="var(--ink)"/>
    <polygon points="212,43 702,43 702,107 212,107 190,75" fill="var(--orange)"/>
    <polygon points="0,873 270,873 300,899 702,899 702,908 0,908" fill="var(--ink)"/>
    <polygon points="300,883 702,883 702,893 310,893" fill="var(--orange)"/>
  </svg>
  <div class="brand"><span class="brand-square"></span>HARLOW LAW LLC</div>

  <div class="letter-body">
    <p class="greeting">Dear sir,</p>
    <p>Lorem Ipsum is simply dummy text of the printing and typesetting industry. Lorem Ipsum has been the industry's standard dummy text ever since the 1500s, when an unknown printer took a galley of type and scrambled it to make a type specimen book. It has survived not only five centuries, but also the leap into electronic typesetting, remaining essentially unchanged.</p>
    <p>It was popularised in the 1960s with the release of transfer lettering sheets containing Lorem Ipsum passages, and more recently with desktop layout software including versions of Lorem Ipsum.</p>
    <p>It is a long established fact that a reader will be distracted by the readable content of a page when looking at its layout. The point of using Lorem Ipsum is that it has a more-or-less normal distribution of letters, as opposed to using 'Content here, content here', making it look like readable English. Many desktop publishing packages and web page editors now use Lorem Ipsum as their default model text, and a search for 'lorem ipsum' will uncover many web sites still in their infancy. Various versions have evolved over the years, sometimes by accident, sometimes on purpose (injected humour and the like)</p>
    <p>Contrary to popular belief, Lorem Ipsum is not simply random text. It has roots in a piece of classical Latin literature from 45 BC, making it over 2000 years old. A Latin professor looked up one of the more obscure Latin words, consectetur, from a Lorem Ipsum passage, and going through the cites of the word in classical literature, discovered the undoubtable source. Lorem Ipsum comes from sections 1.10.32 and 1.10.33 of a classical treatise on the extremes of good and evil, written by an ancient writer in 45 BC. This book is a treatise on the theory of ethics, very popular during the Renaissance. The first line of Lorem Ipsum, "Lorem ipsum dolor sit amet..", comes from a line in section 1.10.32.</p>
    <p>The standard chunk of Lorem Ipsum used since the 1500s is reproduced below for those interested. Sections 1.10.32 and 1.10.33 of that classical treatise are also reproduced in their exact original form, accompanied by English versions from a later translation.</p>
  </div>

  <div class="signature">
    <div class="sig-name"><b>MARCUS</b> DALE</div>
    <div class="sig-role">Lawyer</div>
  </div>

  <div class="contact-row">
    <span class="item phone"><svg class="ico"><use href="#ico-phone"/></svg>014.555.0192</span>
    <span class="item"><svg class="ico"><use href="#ico-pin"/></svg>Your company 1562 address</span>
    <span class="item"><svg class="ico"><use href="#ico-mail"/></svg>harlowlawllc@mail.com</span>
    <span class="item"><svg class="ico"><use href="#ico-web"/></svg>www.harlowlawllc.com</span>
  </div>
</section>

<!-- Second sheet -->
<section class="sheet letter-second">
  <svg class="bands" viewBox="0 0 702 908" preserveAspectRatio="none" aria-hidden="true">
    <rect x="0" y="43" width="62" height="64" fill="var(--ink)"/>
    <polygon points="212,43 702,43 702,107 212,107 190,75" fill="var(--orange)"/>
    <polygon points="0,834 257,834 300,881 702,881 702,908 0,908" fill="var(--ink)"/>
    <polygon points="305,867 702,867 702,876 313,876" fill="var(--orange)"/>
  </svg>
  <div class="brand"><span class="brand-square"></span>HARLOW LAW LLC</div>
  <div class="watermark">HARLOW LAW LLC</div>
  <div class="site-foot">www.harlowlawllc.com</div>
</section>

<!-- Envelope front -->
<section class="sheet envelope-front">
  <svg class="bands" viewBox="0 0 702 352" preserveAspectRatio="none" aria-hidden="true">
    <polygon points="0,308 245,308 285,340 702,340 702,352 0,352" fill="var(--ink)"/>
    <polygon points="280,326 702,326 702,336 290,336" fill="var(--orange)"/>
  </svg>
  <div class="brand"><span class="brand-square"></span>HARLOW LAW LLC</div>
  <div class="address-window"></div>
  <div class="env-contacts col-a">
    <span class="item phone"><svg class="ico"><use href="#ico-phone"/></svg>014.555.0192</span>
    <span class="item"><svg class="ico"><use href="#ico-pin"/></svg>Your company 1562 address</span>
  </div>
  <div class="env-contacts col-b">
    <span class="item"><svg class="ico"><use href="#ico-mail"/></svg>harlowlawllc@mail.com</span>
    <span class="item"><svg class="ico"><use href="#ico-web"/></svg>www.harlowlawllc.com</span>
  </div>
</section>

<!-- Envelope back -->
<section class="sheet envelope-back">
  <svg class="bands" viewBox="0 0 702 352" preserveAspectRatio="none" aria-hidden="true">
    <path d="M6,0 L696,0 L665,70 Q655,86 630,90 L348,133 L70,90 Q45,86 35,70 Z" fill="var(--ink-soft)"/>
    <path d="M6,352 L35,282 Q45,264 72,260 L353,224 L636,260 Q662,264 670,282 L696,352" fill="none" stroke="#ececec" stroke-width="3"/>
  </svg>
  <div class="brand"><span class="brand-square"></span>HARLOW LAW LLC</div>
</section>

<!-- Business card front -->
<section class="sheet card-front">
  <div class="pattern" role="img" aria-label="Dark textured panel with subtle diamond pattern"></div>
  <div class="brand"><span class="brand-square"></span>HARLOW LAW LLC</div>
  <div class="card-info">
    <div class="name"><b>MARCUS</b> DALE</div>
    <div class="role">Lawyer</div>
    <ul>
      <li><svg class="ico"><use href="#ico-phone"/></svg>014.555.0192</li>
      <li><svg class="ico"><use href="#ico-pin"/></svg>Your company 1562 address</li>
      <li><svg class="ico"><use href="#ico-mail"/></svg>harlowlawllc@mail.com</li>
      <li><svg class="ico"><use href="#ico-web"/></svg>www.harlowlawllc.com</li>
    </ul>
  </div>
</section>

<!-- Business card back -->
<section class="sheet card-back">
  <div class="pattern" role="img" aria-label="Dark textured background with faint chevron pattern"></div>
  <div class="brand"><span class="brand-square"></span>HARLOW LAW LLC</div>
  <div class="site">www.harlowlawllc.com</div>
</section>

</body>
</html>
```